Business Card Design Project

Mabel's Tonics is a natural skincare business and we need a business card designed. The company focuses on natural products and will be launching with body scrubs and bath fizzies and our mission statement is: To deliver high quality natural beauty products at a good value. It's two cards - one design - the only information changing would be name and email address

Target Market(s)

Females ages 20-50

Industry/Entity Type

Business

Requirements
Must have
• Mabel's Tonics

Corinne Halvorsen-Pitt
T: 800-417-9368
E: Corinne@MabelsTonics.example
W: www.MabelsTonics.example

Ulrich Benedetti
T: 800-417-9368
E: Ulrich@MabelsTonics.example
W: www.MabelsTonics.example
Nice to have
• I'd like to use the colors or text found at www.mabelstonics.example but I'm open to suggestions since design isn't set in stone yet. I would also like to have the words .....a little bit of magic somewhere under the company name in a different type of font. I would like a design that feels clean and maybe a retro feel to it - front and back would be nice but not mandatory

```html
<!DOCTYPE html>
<html lang="en">
<head>
<meta charset="utf-8">
<title>Mabel's Tonics – Business Cards</title>
<link rel="stylesheet" href="https://fonts.googleapis.com/css2?family=Gilda+Display&family=Arimo:wght@400&family=Poiret+One&display=swap">
<style>
  :root {
    --page: #e4e4e6;
    --cyan: #2fc0ee;
    --blue: #3b86e0;
    --violet: #8a62cc;
    --pink: #e86cb4;
    --magenta: #b21f8e;
    --ink: #1a1a1a;
    --white: #ffffff;
    --card-w: 700px;
    --card-h: 400px;
  }
  * { box-sizing: border-box; margin: 0; padding: 0; }
  html, body {
    width: 1200px; height: 900px; overflow: hidden;
    background: var(--page);
  }
  .sheet {
    position: relative; width: 1200px; height: 900px;
  }
  .card {
    position: absolute; left: 250px;
    width: var(--card-w); height: var(--card-h);
    border-radius: 14px; overflow: hidden;
    box-shadow: 0 6px 18px rgba(0,0,0,0.18);
  }
  .card--back { top: 36px; }
  .card--front { top: 464px; }
  .card__art {
    position: absolute; inset: 0; width: 100%; height: 100%;
  }
  .brand {
    position: absolute;
    font-family: "Gilda Display", Georgia, serif;
    font-size: 64px; line-height: 1;
    color: var(--white);
    white-space: nowrap;
    letter-spacing: 1px;
  }
  .card--back .brand { left: 118px; top: 118px; }
  .card--front .brand { left: 150px; top: 74px; font-size: 58px; }
  .tagline {
    position: absolute; left: 372px; top: 214px;
    font-family: "Poiret One", "Trebuchet MS", sans-serif;
    font-size: 22px; color: var(--magenta);
    letter-spacing: 1px;
  }
  .contact {
    position: absolute; left: 392px; top: 232px;
    font-family: "Arimo", Arial, sans-serif;
    color: var(--ink);
  }
  .contact__name {
    font-size: 21px; color: var(--magenta); margin-bottom: 6px;
    margin-left: -14px;
  }
  .contact__line {
    display: flex; align-items: center; gap: 9px;
    font-size: 15px; line-height: 22px;
  }
  .contact__icon { width: 15px; height: 15px; flex: none; }
</style>
</head>
<body>
<main class="sheet">

  <section class="card card--back" aria-label="Card back">
    <svg class="card__art" viewBox="0 0 700 400" preserveAspectRatio="none">
      <defs>
        <linearGradient id="burst-back" x1="0" y1="0" x2="1" y2="0.3">
          <stop offset="0" stop-color="#2fc0ee"/>
          <stop offset="0.55" stop-color="#3b86e0"/>
          <stop offset="0.8" stop-color="#8a62cc"/>
          <stop offset="1" stop-color="#e86cb4"/>
        </linearGradient>
      </defs>
      <rect width="700" height="400" fill="url(#burst-back)" role="img" aria-label="Radiating light burst with floating bubbles"/>
      <polygon points="0,0 120,0 0,190" fill="var(--magenta)"/>
      <polygon points="700,100 700,400 520,400" fill="var(--magenta)"/>
    </svg>
    <div class="brand">Mabel's Tonics</div>
    <div class="tagline">a little bit of magic</div>
  </section>

  <section class="card card--front" aria-label="Card front">
    <svg class="card__art" viewBox="0 0 700 400" preserveAspectRatio="none">
      <defs>
        <linearGradient id="burst-front" x1="0" y1="0" x2="1" y2="0.3">
          <stop offset="0" stop-color="#2fc0ee"/>
          <stop offset="0.5" stop-color="#3b86e0"/>
          <stop offset="0.78" stop-color="#8a62cc"/>
          <stop offset="1" stop-color="#e86cb4"/>
        </linearGradient>
      </defs>
      <rect width="700" height="400" fill="url(#burst-front)" role="img" aria-label="Radiating light burst with floating bubbles"/>
      <polygon points="545,0 700,0 700,165" fill="var(--magenta)"/>
      <polygon points="0,280 0,400 290,400" fill="var(--magenta)"/>
    </svg>
    <div class="brand">Mabel's Tonics</div>
    <div class="contact">
      <p class="contact__name">Ulrich Benedetti</p>
      <p class="contact__line">
        <svg class="contact__icon" viewBox="0 0 16 16"><path d="M2 5c0-2 2-3 6-3s6 1 6 3v1h-3V4.5H5V6H2z M4 7h8l2 7H2z" fill="var(--ink)"/><circle cx="8" cy="10.5" r="1.8" fill="#ffffff"/></svg>
        <span>800-417-9368</span>
      </p>
      <p class="contact__line">
        <svg class="contact__icon" viewBox="0 0 16 16"><rect x="1" y="3" width="14" height="10" fill="var(--ink)"/><path d="M1.5 3.5L8 9l6.5-5.5" stroke="#ffffff" stroke-width="1.3" fill="none"/></svg>
        <span>Ulrich@MabelsTonics.example</span>
      </p>
      <p class="contact__line">
        <svg class="contact__icon" viewBox="0 0 16 16"><circle cx="8" cy="8" r="6.5" fill="none" stroke="var(--ink)" stroke-width="1.6"/><path d="M1.5 8h13M8 1.5c-3 3.5-3 9.5 0 13M8 1.5c3 3.5 3 9.5 0 13" stroke="var(--ink)" stroke-width="1.2" fill="none"/></svg>
        <span>www.MabelsTonics.example</span>
      </p>
    </div>
  </section>

</main>
</body>
</html>
```